Paper Lantern Theory - Podcast Cover

Paper Lantern Theory is a weekly podcast that dispels some of the myths about conventional economic thinking and provides a new way of thinking about issues that are faced by the global economy. It's insightful, thought-provoking and, most importantly, fun. We are refreshing the look and sound of the podcast. I have attached a copy of the old amateur design (which I did!)

Target Market(s)

Male oriented, smart folk with an interest in politics and economics

Font styles to use
Sans Serif

Requirements
Must have
• Clearly visible title, even when reduced in size. Must be 3000 pixels by 3000 pixels.
Nice to have
• This podcast challenges the status quo. It should reflect that. Photos and names of the hosts. Actually, because th ephotos are so different, we'd be open to the idea of a caricature if you can do that within the price.

```html
<!DOCTYPE html>
<html lang="en">
<head>
<meta charset="UTF-8">
<title>Paper Lantern Theory Podcast – Cover</title>
<link rel="stylesheet" href="https://fonts.googleapis.com/css2?family=Anton&family=Poppins:wght@500&display=swap">
<style>
  :root {
    --ink: #0c0c0e;
    --paper: #ffffff;
    --signal-red: #e81c24;
    --deep-red: #8f0f14;
    --ring-grey: #6f6f72;
    --photo-dark: #3a3a3e;
    --photo-light: #d9d9dc;
  }
  * { margin: 0; padding: 0; box-sizing: border-box; }
  html, body {
    width: 1200px; height: 1200px; overflow: hidden;
    background: var(--ink);
  }
  .cover {
    position: relative;
    width: 1200px; height: 1200px; overflow: hidden;
    background: radial-gradient(ellipse at 50% 40%, #141417 0%, var(--ink) 60%, #0a0a0b 100%);
    font-family: "Anton", "Impact", sans-serif;
    font-weight: 400;
    text-transform: uppercase;
  }
  .title { font-weight: 400; }
  .title-line {
    position: absolute; left: 0; width: 100%;
    display: block;
    text-align: center; line-height: 1;
    white-space: nowrap;
  }
  .title-the {
    top: 73px; font-size: 74px; color: var(--paper);
  }
  .rule {
    position: absolute; top: 112px; height: 3px; background: #000;
  }
  .rule-left { left: 284px; width: 250px; }
  .rule-right { left: 674px; width: 250px; }
  .title-main {
    top: 151px; font-size: 152px; color: var(--paper);
    transform: scaleX(0.84);
  }
  .title-accent {
    top: 301px; font-size: 209px; color: var(--signal-red);
    letter-spacing: 4px;
  }
  .title-podcast {
    top: 525px; font-size: 90px; color: var(--paper);
  }
  .title-with {
    top: 638px; font-size: 50px; color: var(--paper);
  }
  .banknote {
    position: absolute; left: 585px; top: 770px;
    width: 640px; height: 330px;
    transform: rotate(17deg);
    background: linear-gradient(120deg, var(--deep-red) 0%, var(--signal-red) 45%, #c0141b 100%);
    box-shadow: 0 20px 40px rgba(0,0,0,0.6);
  }
  .scatter {
    position: absolute; left: 320px; top: 600px;
    width: 420px; height: 320px;
    background: radial-gradient(ellipse at 70% 70%, rgba(200,20,28,0.3) 0%, rgba(200,20,28,0) 65%);
  }
  .hand {
    position: absolute; right: -40px; top: 770px;
    width: 110px; height: 170px; border-radius: 50px;
    background: linear-gradient(180deg, #e0141c 0%, #a30f15 100%);
  }
  .host-photo {
    position: absolute; top: 737px;
    width: 292px; height: 292px; border-radius: 50%;
    border: 8px solid var(--ring-grey);
  }
  .host-one {
    left: 33px;
    background: linear-gradient(160deg, var(--photo-dark) 0%, #8a8a8e 70%, #e8e8ea 100%);
  }
  .host-two {
    left: 305px;
    background: linear-gradient(180deg, var(--photo-light) 0%, #c99b85 50%, #1f8aa6 100%);
  }
  .host-banner {
    position: absolute; left: 0; top: 1050px;
    width: 600px; height: 68px;
    background: var(--signal-red);
    display: flex; align-items: center; justify-content: center;
  }
  .host-names {
    font-family: "Poppins", "Helvetica Neue", sans-serif;
    font-weight: 500; font-size: 31px; color: var(--paper);
    text-transform: none; letter-spacing: -0.5px;
  }
</style>
</head>
<body>
  <main class="cover">
    <div class="scatter" role="img" aria-label="Red particles dispersing from the banknote"></div>
    <div class="banknote" role="img" aria-label="Red-tinted one dollar banknote dissolving into particles"></div>
    <div class="hand" role="img" aria-label="Hand holding the banknote"></div>

    <span class="rule rule-left"></span>
    <span class="rule rule-right"></span>
    <h1 class="title">
      <span class="title-line title-the">The</span>
      <span class="title-line title-main">Paper Lantern</span>
      <span class="title-line title-accent">Theory</span>
      <span class="title-line title-podcast">Podcast</span>
      <span class="title-line title-with">With</span>
    </h1>

    <div class="host-photo host-one" role="img" aria-label="Portrait photo of host Rowan Hale"></div>
    <div class="host-photo host-two" role="img" aria-label="Portrait photo of host Martin Crewe"></div>

    <div class="host-banner">
      <p class="host-names">Rowan Hale &amp; Martin Crewe</p>
    </div>
  </main>
</body>
</html>
```